Flyer Design Project

Need a DL Size flyer (2 sided) for letter box marketing for our website www.brightwardsecure.com.au

Project Deadline Extended
Reason: Thank you for submitting the designs. We like few of the designs and will request those designers to changes few things to make it more suitable for us. Because of holidays need to extend the deadlines. Thank you.

Industry/Entity Type

Marketing

```html
<!DOCTYPE html>
<html lang="en">
<head>
<meta charset="utf-8">
<title>Brightward Secure – DL Flyer</title>
<link rel="stylesheet" href="https://fonts.googleapis.com/css2?family=Roboto+Condensed:wght@700&family=Arimo:wght@400;700&display=swap">
<style>
  :root {
    --page-bg: #e6e7e9;
    --blue-bright: #1f8ee2;
    --blue-mid: #1a5fb6;
    --navy: #1c2d78;
    --tab-blue: #21408f;
    --yellow: #f7c520;
    --yellow-light: #fbd646;
    --ink: #2b3674;
    --white: #ffffff;
  }
  * { margin: 0; padding: 0; box-sizing: border-box; }
  html, body { width: 1170px; height: 1200px; overflow: hidden; background: var(--page-bg); }
  body { position: relative; font-family: "Arimo", Arial, sans-serif; }

  .flyer-side {
    position: absolute;
    left: 32px;
    width: 1106px;
    height: 553px;
    overflow: hidden;
  }
  .side-front {
    top: 32px;
    background: radial-gradient(ellipse 70% 80% at 48% 58%, var(--blue-bright) 0%, var(--blue-mid) 45%, var(--navy) 100%);
  }
  .side-back { top: 617px; background: var(--navy); }

  .contact-tab {
    position: absolute;
    top: 0; right: 0;
    width: 553px;
    height: 108px;
    background: var(--tab-blue);
    border-bottom-left-radius: 120px 108px;
  }
  .side-back .contact-tab { height: 117px; background: #1f3a8e; }

  .contact-phone {
    position: absolute;
    right: 43px;
    top: 8px;
    color: var(--white);
    font-weight: 700;
    font-size: 38px;
    white-space: nowrap;
  }
  .contact-web {
    position: absolute;
    right: 43px;
    top: 56px;
    color: var(--white);
    font-weight: 700;
    font-size: 25px;
    white-space: nowrap;
  }
  .side-back .contact-phone { top: 20px; font-size: 33px; }
  .side-back .contact-web { top: 64px; font-size: 22px; }

  .brand-name {
    position: absolute;
    left: 57px;
    top: 32px;
    font-family: "Roboto Condensed", "Arial Narrow", sans-serif;
    font-weight: 700;
    font-size: 64px;
    color: var(--yellow);
    line-height: 1;
    white-space: nowrap;
  }
  .brand-tagline {
    position: absolute;
    left: 57px;
    top: 108px;
    font-family: "Roboto Condensed", "Arial Narrow", sans-serif;
    font-weight: 700;
    font-size: 31px;
    color: var(--white);
    letter-spacing: 0.5px;
    white-space: nowrap;
  }
  .side-back .brand-name { left: 19px; top: 20px; font-size: 44px; }
  .side-back .brand-tagline { left: 19px; top: 70px; font-size: 19px; }

  .intro-copy {
    position: absolute;
    left: 57px;
    top: 270px;
    width: 530px;
    color: var(--white);
    font-size: 27px;
    line-height: 35px;
  }

  .product-visual {
    position: absolute;
    left: 610px;
    top: 205px;
    width: 470px;
    height: 348px;
    border-radius: 10px 10px 0 0;
    background: linear-gradient(160deg, #2a2f3a 0%, #6b5a48 45%, #c9a987 70%, #1d2230 100%);
  }

  .guarantee-band {
    position: absolute;
    left: 0; top: 117px;
    width: 100%; height: 315px;
    background: linear-gradient(180deg, var(--yellow-light) 0%, var(--yellow) 100%);
  }
  .guarantee-title {
    position: absolute;
    left: 57px;
    top: 176px;
    font-size: 40px;
    font-weight: 700;
    color: var(--ink);
  }
  .guarantee-list {
    position: absolute;
    left: 57px;
    top: 226px;
    list-style: none;
    color: var(--ink);
    font-weight: 700;
    font-size: 28px;
    line-height: 36px;
  }
  .address {
    position: absolute;
    left: 57px;
    top: 452px;
    color: var(--white);
    font-weight: 700;
    font-size: 28px;
    line-height: 38px;
    font-style: normal;
  }
  .camera-visual {
    position: absolute;
    left: 730px;
    top: 200px;
    width: 360px;
    height: 330px;
    border-radius: 40px;
    background: radial-gradient(ellipse at 45% 40%, #f4f5f7 0%, #c3c7cd 55%, #8a9099 100%);
  }
</style>
</head>
<body>

<section class="flyer-side side-front">
  <div class="contact-tab">
    <span class="contact-phone">Phone: 02 9000 4417</span>
    <span class="contact-web">www.brightwardsecure.com.au</span>
  </div>
  <h1 class="brand-name">Brightward Secure</h1>
  <p class="brand-tagline">CCTV System Specialist</p>
  <p class="intro-copy">Brightward Secure is dedicated to providing high quality CCTV System at affordable prices. All of our packages include hardware, software, accessories and full installation.</p>
  <div class="product-visual" role="img" aria-label="Monitor showing multi-camera CCTV feeds with a hand holding a smartphone viewing the same feeds"></div>
</section>

<section class="flyer-side side-back">
  <div class="contact-tab">
    <span class="contact-phone">Phone: 02 9000 4417</span>
    <span class="contact-web">www.brightwardsecure.com.au</span>
  </div>
  <h2 class="brand-name">Brightward Secure</h2>
  <p class="brand-tagline">CCTV System Specialist</p>
  <div class="guarantee-band"></div>
  <h3 class="guarantee-title">Our Guarantee</h3>
  <ul class="guarantee-list">
    <li>High quality hardware</li>
    <li>100% customer satisfaction</li>
    <li>1 year full warranty</li>
    <li>14 days money back guarantee</li>
  </ul>
  <address class="address">7/4 Harrow Lane, Bankstown,<br>NSW 2200</address>
  <div class="camera-visual" role="img" aria-label="White bullet-style CCTV security camera on a wall mount bracket"></div>
</section>

</body>
</html>
```